A resource brochure for seniors and their families/Maplecrest Resource Group

As we age, the journey can come with unexpected challenges and obstacles. Maplecrest Resource Group is here to provide seniors and their families with a road map to navigate those challenges and insure the journey is as smooth as possible. We are a company that offers 'one stop shop' resources for seniors who need assistance with selling their home, need home care support or need to find suitable senior housing living choices and much more. We need this brochure to showcase a caring, clear and clear way for families or individuals, many who have just lost a spouse/parent, to find resources during a very difficult and confusing time in their life. The final design should communicate caring support, a call to action (call us!), and showcase a professional and knowledgeable team that will gently support and be a guide to families and individuals who are trying to make big life choices within the senior care arena.
Updates

Project Deadline Extended Reason: To give more time for designers as the initial window seemed a little too short. Thank you!!! Added Friday, March 20, 2015

Target Market(s)

A mature market- SENIORS (75+) and their families (adult children 50+) who typically are going through life changes such as losing a spouse or having to make a move from their home into a Retirement Community.

Industry/Entity Type

Group

Font styles to use
Serif
Script

Requirements
Must have
• Showcase a thoughtful and caring mentality- 'we will take care of you" in a professional and knowledgeable way. Please make it clear what the message is - we can assist with selling a home, bringing support and care into the home, find more appropriate housing as well as any resources or tools needed throughout the senior care spectrum of resources. Must have our name, logo, website and address and we need one panel to be laid out as a mailer- our address on top left. (Please see attached rough draft for address- thank you!) Also- please keep the testimonial, which is attached inclusive of additional verbiage.
Nice to have
• An attractive senior (female) on the cover of the brochure with a 'What's Next?" feel to engage people to open the collateral and relate to the story and purpose of what we do. Showcase what our services are- we are a company that guides families to and through much needed resources as it relates to aging and the ever-changing needs of an elderly person. We want to be the experts and trusted by our clients and the tough decisions that come along with aging. We offer our referral services at no cost to our clients.
Should not have
• Should not sound slick, 'sales-y' or too pushy- we are trying to build a relationship and not 'over sell'...we want to be a trusted resource guide and a helping hand.

```html
<!DOCTYPE html>
<html lang="en">
<head>
<meta charset="utf-8">
<title>Maplecrest Senior Resource Group – Brochure Outside</title>
<link rel="stylesheet" href="https://fonts.googleapis.com/css2?family=Crimson+Text&family=Montserrat:wght@500&family=Nunito:wght@900&family=Open+Sans:wght@400;700&family=Fira+Sans+Condensed:ital,wght@1,600&display=swap">
<style>
  :root {
    --cream: #faebd5;
    --purple: #57335f;
    --orange: #fbb12e;
    --gray: #d3d4d6;
    --navy: #2e2f4f;
    --ink: #1f1f24;
    --white: #ffffff;
    --call-text: #e9e4ec;
  }
  html, body {
    margin: 0;
    padding: 0;
    width: 1200px;
    height: 1000px;
    overflow: hidden;
    background: var(--white);
  }
  .brochure {
    position: absolute;
    left: 75px;
    top: 85px;
    width: 1060px;
    height: 815px;
    background: var(--cream);
    overflow: hidden;
  }
  .brochure-shapes {
    position: absolute;
    left: 0;
    top: 0;
  }
  .call-us {
    position: absolute;
    left: 43px;
    top: 76px;
    color: var(--call-text);
  }
  .call-us__label {
    font-family: "Montserrat", sans-serif;
    font-weight: 500;
    font-size: 23px;
    letter-spacing: 0.5px;
  }
  .call-us__number {
    font-family: "Fira Sans Condensed", sans-serif;
    font-style: italic;
    font-weight: 600;
    font-size: 33px;
    margin-top: 2px;
  }
  .brand {
    position: absolute;
    text-align: center;
    font-family: "Crimson Text", serif;
    color: var(--navy);
    line-height: 1;
  }
  .brand__mark {
    display: block;
    width: 22px;
    height: 22px;
    border-radius: 50%;
    background: var(--orange);
    margin: 0 auto 14px;
  }
  .brand__name { font-size: 37px; }
  .brand__tag { font-size: 25px; margin-top: 6px; }
  .brand--back { left: 40px; width: 310px; top: 400px; }
  .brand--cover { left: 728px; width: 310px; top: 630px; }
  .brand--cover .brand__name { font-size: 39px; }
  .contact {
    position: absolute;
    left: 40px;
    width: 310px;
    top: 528px;
    text-align: center;
    font-family: "Open Sans", sans-serif;
    color: var(--ink);
    font-size: 14.5px;
    line-height: 19.5px;
  }
  .contact__title {
    font-weight: 700;
    font-size: 17px;
    margin: 0 0 14px;
  }
  .contact__label {
    font-weight: 700;
    font-size: 15px;
    margin: 0;
  }
  .contact__block { margin: 0 0 12px; }
  .mailer-brand {
    position: absolute;
    left: 435px;
    top: 770px;
    width: 230px;
    transform-origin: top left;
    transform: rotate(-90deg);
    font-family: "Crimson Text", serif;
    color: var(--navy);
    text-align: center;
    line-height: 1;
  }
  .mailer-brand .brand__name { font-size: 31px; }
  .mailer-brand .brand__tag { font-size: 20px; margin-top: 4px; }
  .mailer-address {
    position: absolute;
    left: 513px;
    top: 735px;
    width: 150px;
    transform-origin: top left;
    transform: rotate(-90deg);
    font-family: "Open Sans", sans-serif;
    font-size: 11.5px;
    line-height: 15px;
    color: var(--ink);
    text-align: right;
    border-top: 1px solid var(--ink);
    border-bottom: 1px solid var(--ink);
    padding: 3px 0;
  }
  .mailer-address p { margin: 0; white-space: nowrap; }
</style>
</head>
<body>
<main class="brochure">
  <svg class="brochure-shapes" width="1060" height="815" viewBox="0 0 1060 815">
    <defs>
      <linearGradient id="photoTones" x1="0" y1="0" x2="1" y2="1">
        <stop offset="0" stop-color="#c9c6c0"/>
        <stop offset="0.4" stop-color="#d9a982"/>
        <stop offset="0.75" stop-color="#41557a"/>
        <stop offset="1" stop-color="#e9ddd0"/>
      </linearGradient>
      <clipPath id="panelClip"><rect width="1060" height="815"/></clipPath>
    </defs>
    <g clip-path="url(#panelClip)">
      <path class="band band--gray" d="M0 0 H355 C345 170 220 360 0 420 Z" fill="var(--gray)"/>
      <path class="band band--orange" d="M0 0 H345 C325 150 200 310 0 335 Z" fill="var(--orange)"/>
      <path class="band band--purple" d="M0 0 H330 C300 150 170 250 0 255 Z" fill="var(--purple)"/>
      <path class="sweep sweep--gray" d="M515 0 H622 C630 240 680 400 775 505 C640 420 545 260 515 0 Z" fill="var(--gray)"/>
      <ellipse class="cover-ring" cx="985" cy="270" rx="320" ry="315" fill="var(--orange)"/>
      <ellipse class="cover-photo" cx="1010" cy="280" rx="277" ry="275" fill="url(#photoTones)" role="img" aria-label="Photo of a smiling senior woman resting her arms on a sofa"/>
      <text class="cover-headline" x="903" y="435" text-anchor="middle" font-family="Nunito, sans-serif" font-weight="900" font-size="60" fill="var(--navy)" stroke="var(--white)" stroke-width="5" paint-order="stroke" stroke-linejoin="round">
        <tspan x="903" dy="0">What’s</tspan>
        <tspan x="903" dy="58">Next?</tspan>
      </text>
    </g>
  </svg>

  <div class="call-us">
    <div class="call-us__label">CALL US:</div>
    <div class="call-us__number">(800) 555-0142</div>
  </div>

  <div class="brand brand--back">
    <span class="brand__mark"></span>
    <div class="brand__name">Maplecrest</div>
    <div class="brand__tag">Senior Resource Group</div>
  </div>

  <section class="contact">
    <h2 class="contact__title">CONTACT INFORMATION</h2>
    <div class="contact__block">
      <h3 class="contact__label">ADDRESS</h3>
      4820 Alder Crest Road<br>Suite C310<br>Everly, WA 98120
    </div>
    <div class="contact__block">
      <h3 class="contact__label">EMAIL</h3>
      hello@maplecrestSRG.com
    </div>
    <div class="contact__block">
      <h3 class="contact__label">PHONE</h3>
      (800) 555-0142
    </div>
  </section>

  <div class="mailer-brand">
    <div class="brand__name">Maplecrest</div>
    <div class="brand__tag">Senior Resource Group</div>
  </div>
  <div class="mailer-address">
    <p>4820 Alder Crest Road</p>
    <p>Suite C310</p>
    <p>Everly, WA 98120</p>
    <p>(800) 555-0144</p>
    <p>info@MaplecrestSRG.com</p>
  </div>

  <div class="brand brand--cover">
    <span class="brand__mark"></span>
    <div class="brand__name">Maplecrest</div>
    <div class="brand__tag">Senior Resource Group</div>
  </div>
</main>
</body>
</html>
```